K & D A/C Compressors' Business Card

Hello,

I need someone to create a new business card for my business. The name of my Business is: K & D A/C Compressors. I sell automotive air conditioning parts (a/c parts). I would like the business card to incorporate my logo, and to have an automotive feel to it. It is important that the business card feel like it is coming from an automotive parts business.

I already have a logo, which I will provide.

Thanks.
Updates

Project Deadline Extended Reason: I feel like extending the deadline until October 9, 2017, will allow for more time to design the business card. Thank you for your understanding. Added Monday, October 2, 2017

Target Market(s)

Consumers who need automotive a/c parts, and auto mechanics.

Industry/Entity Type

Automotive

Contact Information for Business Card

Business name: K & D A/C Compressors
Business Address: 48207 Southwest 36th Street, Coral Harbor, Florida 33990
Telephone: 305-472-1390
Fax: To be provided once I choose your design.
Website: www.kdcoolunits.example
Email: support@kdcoolunits.example
Names: To be provided once I choose your design.

Font styles to use
Sans Serif

Colors

Designer to choose colors to be used in the design.

Requirements
Must have
• The business card must include all of the "Business Card Details" and the logo I have uploaded.

```html
<!DOCTYPE html>
<html lang="en">
<head>
<meta charset="utf-8">
<title>K &amp; D A/C Compressors – Business Card</title>
<link href="https://fonts.googleapis.com/css2?family=Montserrat:wght@500;600;700&family=Mulish:wght@400;600&display=swap" rel="stylesheet">
<style>
  :root {
    --page-bg: #e9e8e6;
    --brand-blue: #00a8e8;
    --blue-light: #1fb0ea;
    --blue-deep: #066c9c;
    --steel: #5e6063;
    --steel-light: #a7a9ac;
    --logo-grey: #9b9da0;
    --card-white: #ffffff;
    --logo-pale: #d6eef9;
  }
  * { box-sizing: border-box; margin: 0; padding: 0; }
  html, body { width: 1200px; height: 1200px; overflow: hidden; background: var(--page-bg); }
  .canvas { position: relative; width: 1200px; height: 1200px; }
  .card {
    position: absolute; left: 170px; width: 860px; height: 491px;
    box-shadow: 0 6px 20px rgba(0,0,0,.18); overflow: hidden;
  }
  .card--front { top: 80px; background: radial-gradient(ellipse at 42% 45%, var(--blue-light) 0%, #0b93cf 45%, var(--blue-deep) 100%); }
  .card--back { top: 629px; background: var(--card-white); }

  .brand {
    position: absolute; left: 0; right: 0; display: flex; align-items: center; justify-content: center; gap: 16px;
    font-family: "Montserrat", sans-serif; font-weight: 600; white-space: nowrap;
  }
  .brand__mark { width: 22px; height: 22px; }
  .card--front .brand { top: 212px; font-size: 44px; color: var(--logo-pale); }
  .card--front .brand__mark { background: var(--logo-pale); }
  .card--back .brand { top: 62px; font-size: 36px; color: var(--logo-grey); }
  .card--back .brand__mark { background: var(--logo-grey); width: 18px; height: 18px; }

  .holder {
    position: absolute; top: 150px; left: 0; right: 0; text-align: center;
    font-family: "Montserrat", sans-serif; color: var(--brand-blue);
  }
  .holder__name { font-weight: 700; font-size: 30px; letter-spacing: .5px; }
  .holder__sep { font-weight: 700; font-size: 30px; margin: 0 8px; }
  .holder__role { font-family: "Mulish", sans-serif; font-weight: 600; font-size: 20px; }

  .bands { position: absolute; left: 0; top: 0; width: 860px; height: 491px; }
  .band-text { font-family: "Mulish", sans-serif; font-size: 17px; fill: #ffffff; }

  .address {
    position: absolute; left: 0; right: 0; top: 420px; text-align: center;
    font-family: "Mulish", sans-serif; font-size: 22px; color: var(--brand-blue); white-space: nowrap;
  }
</style>
</head>
<body>
<main class="canvas">
  <section class="card card--front" aria-label="Card front">
    <div class="brand"><span class="brand__mark"></span><span>K &amp; D A/C Compressors</span></div>
  </section>

  <section class="card card--back" aria-label="Card back">
    <div class="brand"><span class="brand__mark"></span><span>K &amp; D A/C Compressors</span></div>

    <div class="holder">
      <span class="holder__name">JOHN DOE</span><span class="holder__sep">|</span><span class="holder__role">Director</span>
    </div>

    <svg class="bands" viewBox="0 0 860 491">
      <polygon points="468,236 860,236 860,322 468,322 452,279" fill="var(--steel)"/>
      <polygon points="478,246 860,246 860,306 478,306 466,276" fill="var(--brand-blue)"/>
      <polygon points="0,316 392,316 408,359 392,402 0,402" fill="var(--steel)"/>
      <polygon points="0,330 382,330 394,360 382,390 0,390" fill="var(--brand-blue)"/>
      <polygon points="430,282 465,302 465,340 430,360 395,340 395,302" fill="#ffffff"/>
      <polygon points="430,290 458,306 458,336 430,352 402,336 402,306" fill="var(--steel-light)"/>

      <rect x="502" y="259" width="14" height="10" rx="2" fill="#fff"/>
      <rect x="505" y="255" width="8" height="5" fill="#fff"/>
      <text class="band-text" x="526" y="270">xxx-xxx-xxxx</text>
      <circle cx="509" cy="289" r="7" fill="none" stroke="#fff" stroke-width="2"/>
      <line x1="502" y1="289" x2="516" y2="289" stroke="#fff" stroke-width="1.5"/>
      <text class="band-text" x="526" y="295">www.kdcoolunits.example</text>

      <text class="band-text" x="350" y="356" text-anchor="end">305-472-1390</text>
      <path d="M361 343 q2 -2 4 0 l3 4 q1 2 -1 3 q2 4 6 6 q1 -2 3 -1 l4 3 q2 2 0 4 q-3 3 -7 1 q-9 -5 -13 -13 q-2 -4 1 -7z" fill="#fff"/>
      <text class="band-text" x="350" y="380" text-anchor="end">support@kdcoolunits.example</text>
      <rect x="360" y="368" width="18" height="13" fill="#fff"/>
    </svg>

    <p class="address">48207 Southwest 36th Street, Coral Harbor, Florida 33990</p>
  </section>
</main>
</body>
</html>
```